Medical Cannabis company is looking for a LOGO design *

SILVER PETALWORKS (SP) is a new company in the Israeli medical cannabis industry. We will engage in PREMIUM medical cannabis growing and cultivation and also manufacturing of HIGH-END cannabis based medical products.
the design should reflect luxury, high-end and Pharma-grade products.
the design should use color GOLD and NOT using the famous cannabis leaf !

Target Market(s)

international medical cannabis Pharmaceutical companies
and of course local and international patients

Contact Information for Business Card

Yoav Ben-Ami
Founder and CEO

Silver Petalworks
Medical grade cannabis

yoavbenami@mailnest.example
972-52-3186907

Colors
ffc214
fbed22

Requirements
Must have
• clean and simple
• luxury
• gold !!
• (can also have green for Cannabis and/or blue for Pharma)
Should not have
• cannabis leaf

```html
<!DOCTYPE html>
<html lang="en">
<head>
<meta charset="utf-8">
<title>Silver Petalworks — Business Cards</title>
<link rel="stylesheet" href="https://fonts.googleapis.com/css2?family=Lato:wght@400&display=swap">
<style>
  :root {
    --backdrop: #4d5567;
    --card: #ffffff;
    --yellow: #ffc214;
    --gold: #b8894f;
    --gold-light: #f3cf8f;
    --gold-dark: #9a6f3a;
    --ink: #1f1d1d;
    --ink-soft: #3a3a3a;
  }
  html, body {
    margin: 0;
    padding: 0;
    width: 1200px;
    height: 1000px;
    overflow: hidden;
    background: var(--backdrop);
    font-family: "Lato", Arial, sans-serif;
  }
  .canvas { position: relative; width: 1200px; height: 1000px; }
  .card {
    position: absolute;
    background: var(--card);
    overflow: hidden;
  }
  .card--rounded { border-radius: 30px; }
  .card--front-a { left: 65px; top: 103px; width: 513px; height: 292px; }
  .card--back-a  { left: 65px; top: 447px; width: 513px; height: 293px; }
  .card--front-b { left: 622px; top: 260px; width: 516px; height: 295px; }
  .card--back-b  { left: 622px; top: 604px; width: 516px; height: 294px; }

  .brand-front {
    position: absolute;
    inset: 0;
    display: flex;
    flex-direction: column;
    align-items: center;
    justify-content: center;
    gap: 22px;
    padding-top: 8px;
  }
  .brand-front__mark {
    width: 62px; height: 62px;
    border-radius: 50%;
    background: var(--gold);
  }
  .brand-front__name {
    color: var(--gold);
    font-size: 27px;
    letter-spacing: 1.5px;
    font-weight: 400;
  }

  .wave { position: absolute; inset: 0; width: 100%; height: 100%; }

  .person { position: absolute; left: 27px; top: 80px; }
  .person__name { font-size: 25px; color: var(--ink); line-height: 1; }
  .person__role { font-size: 15px; color: var(--ink-soft); margin-top: 12px; }

  .contact { position: absolute; left: 27px; top: 193px; list-style: none; margin: 0; padding: 0; }
  .contact__item {
    display: flex; align-items: center; gap: 11px;
    font-size: 17.5px; color: var(--ink); height: 29px;
  }
  .contact__icon { width: 13px; height: 13px; flex: none; fill: var(--ink); }

  .brand-back {
    position: absolute; right: 22px; top: 132px;
    width: 200px;
    display: flex; flex-direction: column; align-items: center;
    color: var(--ink);
  }
  .brand-back__mark { width: 46px; height: 46px; border-radius: 50%; background: var(--ink); margin-bottom: 18px; }
  .brand-back__name { font-size: 16.5px; letter-spacing: 0.3px; }
  .brand-back__tagline { font-size: 15px; margin-top: 3px; }
</style>
</head>
<body>
<div class="canvas">

  <section class="card card--rounded card--front-a">
    <div class="brand-front">
      <span class="brand-front__mark"></span>
      <span class="brand-front__name">SILVER PETALWORKS</span>
    </div>
  </section>

  <section class="card card--rounded card--back-a">
    <svg class="wave" viewBox="0 0 513 293" preserveAspectRatio="none" aria-hidden="true">
      <defs>
        <linearGradient id="ribbonA" x1="0" y1="0" x2="1" y2="0">
          <stop offset="0" stop-color="var(--gold-dark)"/>
          <stop offset="0.55" stop-color="var(--gold)"/>
          <stop offset="0.78" stop-color="var(--gold-light)"/>
          <stop offset="1" stop-color="var(--gold)"/>
        </linearGradient>
      </defs>
      <path fill="var(--yellow)" d="M0,0 H513 V98 C440,62 360,78 280,118 C210,153 150,180 90,180 C55,180 25,170 0,155 Z"/>
      <path fill="url(#ribbonA)" d="M90,180 C150,180 210,153 280,118 C360,78 440,62 513,98 V114 C450,84 380,96 300,134 C220,172 160,184 90,180 Z"/>
    </svg>
    <div class="person">
      <div class="person__name">Yoav Ben-Ami</div>
      <div class="person__role">Founder and CEO</div>
    </div>
    <ul class="contact">
      <li class="contact__item"><svg class="contact__icon" viewBox="0 0 24 24"><path d="M6.6 10.8a15.1 15.1 0 0 0 6.6 6.6l2.2-2.2c.3-.3.7-.4 1-.2 1.1.4 2.3.6 3.6.6.6 0 1 .4 1 1V20c0 .6-.4 1-1 1A17 17 0 0 1 3 4c0-.6.4-1 1-1h3.5c.6 0 1 .4 1 1 0 1.3.2 2.5.6 3.6.1.3 0 .7-.2 1z"/></svg>972-52-3186907</li>
      <li class="contact__item"><svg class="contact__icon" viewBox="0 0 24 24"><path d="M2 5h20v14H2z M3.5 6.5 12 12.5l8.5-6z" fill-rule="evenodd"/></svg>yoavbenami@mailnest.example</li>
    </ul>
    <div class="brand-back">
      <span class="brand-back__mark"></span>
      <span class="brand-back__name">SILVER PETALWORKS</span>
      <span class="brand-back__tagline">Medical grade cannabis</span>
    </div>
  </section>

  <section class="card card--front-b">
    <div class="brand-front">
      <span class="brand-front__mark"></span>
      <span class="brand-front__name">SILVER PETALWORKS</span>
    </div>
  </section>

  <section class="card card--back-b">
    <svg class="wave" viewBox="0 0 516 294" preserveAspectRatio="none" aria-hidden="true">
      <defs>
        <linearGradient id="ribbonB" x1="0" y1="0" x2="1" y2="0">
          <stop offset="0" stop-color="var(--gold-dark)"/>
          <stop offset="0.55" stop-color="var(--gold)"/>
          <stop offset="0.78" stop-color="var(--gold-light)"/>
          <stop offset="1" stop-color="var(--gold)"/>
        </linearGradient>
      </defs>
      <path fill="var(--yellow)" d="M0,0 H516 V98 C442,62 362,78 282,118 C212,153 152,180 92,180 C56,180 26,170 0,155 Z"/>
      <path fill="url(#ribbonB)" d="M92,180 C152,180 212,153 282,118 C362,78 442,62 516,98 V114 C452,84 382,96 302,134 C222,172 162,184 92,180 Z"/>
    </svg>
    <div class="person">
      <div class="person__name">Yoav Ben-Ami</div>
      <div class="person__role">Founder and CEO</div>
    </div>
    <ul class="contact">
      <li class="contact__item"><svg class="contact__icon" viewBox="0 0 24 24"><path d="M6.6 10.8a15.1 15.1 0 0 0 6.6 6.6l2.2-2.2c.3-.3.7-.4 1-.2 1.1.4 2.3.6 3.6.6.6 0 1 .4 1 1V20c0 .6-.4 1-1 1A17 17 0 0 1 3 4c0-.6.4-1 1-1h3.5c.6 0 1 .4 1 1 0 1.3.2 2.5.6 3.6.1.3 0 .7-.2 1z"/></svg>972-52-3186907</li>
      <li class="contact__item"><svg class="contact__icon" viewBox="0 0 24 24"><path d="M2 5h20v14H2z M3.5 6.5 12 12.5l8.5-6z" fill-rule="evenodd"/></svg>yoavbenami@mailnest.example</li>
    </ul>
    <div class="brand-back">
      <span class="brand-back__mark"></span>
      <span class="brand-back__name">SILVER PETALWORKS</span>
      <span class="brand-back__tagline">Medical grade cannabis</span>
    </div>
  </section>

</div>
</body>
</html>
```